Autodetailing namecard design: Rose Gold Lettering on Black Matt

This is a namecard design project
requiring two-sided design
Base Color of Namecard: black matt

On front:
Company name,
"Lumina Finishes 14 Cendana"
Subtext: Auto Detailing Studio

Name of card holder: Marcus Oyelaran
Phone Number: +6011-4837-5062
address: 14, Jalan Cendana 5/3Taman Seri Cendana, 81400 Johor Bahru, Johor, Malaysia

Back:
Our Services
High Gloss Car Paint Protection
Custom Color Modification and Styling
Anti-Chip Glass Protection Film
Heat Rejection Glass Tinting

Target Market(s)

Autodetailing for highend cars

Contact Information for Business Card

as mentioned in project details

Colors

Designer to choose colors to be used in the design.

Requirements
Must have
• The main value-add to this project is the design of a logo suited for our purpose and name, and the inclusion of business card details into the card design

```html
<!DOCTYPE html>
<html lang="en">
<head>
<meta charset="utf-8">
<title>Lumina Finishes 14 Cendana – Name Card</title>
<link rel="stylesheet" href="https://fonts.googleapis.com/css2?family=Exo+2:wght@600;700&family=Roboto+Condensed:wght@400&display=swap">
<style>
  :root {
    --stage: #6a6a6a;
    --card: #1b1b1b;
    --card-edge: #262626;
    --rose-gold: #c4917b;
    --rose-gold-soft: #b88a75;
    --text-light: #f2f2f2;
    --text-muted: #c9c9c9;
  }
  * { margin: 0; padding: 0; box-sizing: border-box; }
  html, body { width: 1200px; height: 568px; overflow: hidden; }
  body {
    background: var(--stage);
    position: relative;
    font-family: "Roboto Condensed", Arial, sans-serif;
  }
  .card {
    position: absolute;
    top: 154px;
    width: 430px;
    height: 260px;
    border-radius: 10px;
    background: radial-gradient(ellipse at 40% 35%, #232323 0%, var(--card) 70%);
    border: 1px solid var(--card-edge);
    box-shadow: 0 2px 6px rgba(0,0,0,0.25);
  }
  .card--services { left: 140px; }
  .card--contact { left: 630px; }

  .brand {
    position: absolute;
    left: 26px;
    top: 96px;
    width: 180px;
    text-align: center;
    color: var(--rose-gold);
  }
  .card--contact .brand { left: 26px; top: 102px; width: 164px; }
  .brand__name {
    font-family: "Exo 2", Arial, sans-serif;
    font-weight: 700;
    text-transform: uppercase;
    font-size: 19px;
    line-height: 20px;
    letter-spacing: 0.5px;
  }
  .card--contact .brand__name { font-size: 17px; line-height: 18px; }
  .brand__tagline {
    margin-top: 5px;
    font-family: "Exo 2", Arial, sans-serif;
    font-weight: 600;
    font-size: 7px;
    letter-spacing: 1px;
    text-transform: uppercase;
    color: var(--rose-gold-soft);
  }

  .services { position: absolute; left: 230px; top: 76px; }
  .services__title,
  .contact__name {
    font-family: "Exo 2", Arial, sans-serif;
    font-weight: 600;
    font-size: 18px;
    color: var(--rose-gold);
    letter-spacing: 0.3px;
  }
  .services__list { list-style: none; margin-top: 13px; }
  .services__item {
    font-size: 11.5px;
    line-height: 17.6px;
    color: var(--text-light);
  }
  .services__item::before { content: "»"; margin-right: 6px; }

  .contact { position: absolute; left: 211px; top: 88px; }
  .contact__details {
    margin-top: 6px;
    font-size: 11.5px;
    line-height: 17.2px;
    color: var(--text-muted);
  }
</style>
</head>
<body>
  <section class="card card--services">
    <div class="brand">
      <div class="brand__name">Lumina Finishes<br>14 Cendana</div>
      <div class="brand__tagline">Auto Detailing Studio</div>
    </div>
    <div class="services">
      <h2 class="services__title">Our Services</h2>
      <ul class="services__list">
        <li class="services__item">High Gloss Car Paint Protection</li>
        <li class="services__item">Custom Color Modification &amp; Styling</li>
        <li class="services__item">Anti-Chip Glass Protection Film</li>
        <li class="services__item">Heat Rejection Glass Tinting</li>
      </ul>
    </div>
  </section>

  <section class="card card--contact">
    <div class="brand">
      <div class="brand__name">Lumina Finishes<br>14 Cendana</div>
      <div class="brand__tagline">Auto Detailing Studio</div>
    </div>
    <div class="contact">
      <h1 class="contact__name">Marcus Oyelaran</h1>
      <p class="contact__details">
        +6011-4837-5062<br>
        14, Jalan Cendana 5/3Taman Seri Cendana,<br>
        81400 Johor Bahru, Johor, Malaysia
      </p>
    </div>
  </section>
</body>
</html>
```